ARC VOLLEY Business Card Project

I'd like to request a business card design for the new company I've launched.
The name of the company is "ARC VOLLEY" an indoor unmanned tennis practice facility.
We would like to see designs that use our brand identity color in the logo I've attached.
We hope to get the design with modern, luxurious and elegant tone and manner.
We hope the logo should not be too big.

Business card must have elements as below:
- Logo (One of the logos I've attached)
- Name (In Korean Text) : 박 서 윤
- Title (In Korean Text) : 대표
- Phone Number : 010-8472-3916
- Email Address : seoyun.park@arcvolley-example.co.kr
- Website : www.arcvolley-example.co.kr
- Instagram : arcvolley
- Address (In Korean text) : 경기도 용인시 수지구 풍덕천로 456 미래타워 5층 501호, 502호

Target Market(s)

Tennis amateurs in 20 to 40s

Industry/Entity Type

Sports, Hobby

Contact Information for Business Card

- Logo (One of the logos I've attached) - Name (In Korean Text) : 박 서 윤 - Title (In Korean Text) : 대표 - Phone Number : 010-8472-3916 - Email Address : seoyun.park@arcvolley-example.co.kr - Website : www.arcvolley-example.co.kr - Instagram : arcvolley - Address (In Korean text) : 경기도 용인시 수지구 풍덕천로 456 미래타워 5층 501호, 502호

Font styles to use
Sans Serif

Requirements
Must have
• Double sided
Nice to have
• Logo with intaglio or relief embossing
Should not have
• Logo should not be too big.

```html
<!DOCTYPE html>
<html lang="ko">
<head>
<meta charset="utf-8">
<title>ARC VOLLEY Business Card</title>
<link href="https://fonts.googleapis.com/css2?family=Poppins:wght@400;500;600&family=Noto+Sans+KR:wght@400;500&display=swap" rel="stylesheet">
<style>
  :root {
    --backdrop: #a7a7a7;
    --paper: #ffffff;
    --brand-green: #2c4d33;
    --ink: #2a2a2a;
    --rule: #b9c4c0;
    --ghost: #eef0ee;
    --band-dark: #3f3f42;
  }
  html, body {
    margin: 0;
    padding: 0;
    width: 1200px;
    height: 2415px;
    overflow: hidden;
    background: var(--backdrop);
  }
  .canvas {
    position: relative;
    width: 1200px;
    height: 2415px;
  }
  .card {
    position: absolute;
    left: 112px;
    width: 976px;
    height: 556px;
    background: var(--paper);
    box-shadow: 0 6px 30px rgba(0,0,0,0.22);
    overflow: hidden;
  }
  .card--front { top: 606px; }
  .card--back { top: 1752px; }

  .ghost-mark {
    position: absolute;
    border-radius: 50%;
    background: var(--ghost);
  }
  .card--front .ghost-mark { left: 640px; top: 127px; width: 300px; height: 300px; }
  .card--back .ghost-mark { left: 556px; top: 86px; width: 236px; height: 236px; }

  .wordmark {
    position: absolute;
    font-family: 'Poppins', sans-serif;
    font-weight: 600;
    color: var(--brand-green);
    letter-spacing: 0.02em;
    white-space: nowrap;
    line-height: 1;
  }
  .card--front .wordmark { left: 156px; top: 244px; font-size: 52px; }
  .card--back .wordmark { left: 80px; top: 130px; font-size: 36px; }

  .person-name {
    position: absolute;
    left: 82px;
    top: 250px;
    margin: 0;
    font-family: 'Noto Sans KR', sans-serif;
    font-weight: 500;
    font-size: 32px;
    color: var(--ink);
    line-height: 1;
  }
  .person-title {
    position: absolute;
    left: 82px;
    top: 300px;
    margin: 0;
    font-family: 'Noto Sans KR', sans-serif;
    font-weight: 400;
    font-size: 26px;
    color: var(--ink);
    line-height: 1;
  }
  .divider {
    position: absolute;
    left: 76px;
    top: 346px;
    width: 815px;
    height: 1px;
    background: var(--rule);
  }
  .contact-list {
    position: absolute;
    left: 80px;
    top: 372px;
    display: grid;
    grid-template-columns: 300px auto;
    row-gap: 16px;
  }
  .contact {
    display: flex;
    align-items: center;
    gap: 10px;
    font-family: 'Poppins', sans-serif;
    font-size: 22px;
    color: var(--ink);
    white-space: nowrap;
    line-height: 1.2;
  }
  .contact--address {
    grid-column: 1 / span 2;
    font-family: 'Noto Sans KR', sans-serif;
    font-size: 20px;
  }
  .contact svg { width: 22px; height: 22px; flex: none; }

  .band {
    position: absolute;
    bottom: 0;
  }
  .band--green { left: 0; width: 552px; height: 14px; background: var(--brand-green); clip-path: polygon(0 0, 98.6% 0, 100% 100%, 0 100%); }
  .band--dark { left: 556px; right: 0; height: 8px; background: var(--band-dark); }
</style>
</head>
<body>
<div class="canvas">

  <section class="card card--front" aria-label="Card front">
    <div class="ghost-mark" aria-hidden="true"></div>
    <div class="wordmark">ARC VOLLEY</div>
  </section>

  <section class="card card--back" aria-label="Card back">
    <div class="ghost-mark" aria-hidden="true"></div>
    <div class="wordmark">ARC VOLLEY</div>
    <h1 class="person-name">박 서 윤</h1>
    <p class="person-title">대표</p>
    <div class="divider"></div>
    <div class="contact-list">
      <div class="contact contact--phone">
        <svg viewBox="0 0 24 24" aria-hidden="true"><path fill="var(--brand-green)" d="M6.6 10.8a15.1 15.1 0 0 0 6.6 6.6l2.2-2.2c.3-.3.7-.4 1-.2 1.1.4 2.3.6 3.6.6.6 0 1 .4 1 1V20c0 .6-.4 1-1 1A17 17 0 0 1 3 4c0-.6.4-1 1-1h3.5c.6 0 1 .4 1 1 0 1.3.2 2.5.6 3.6.1.3 0 .7-.2 1z"/></svg>
        <span>010-8472-3916</span>
      </div>
      <div class="contact contact--email">
        <svg viewBox="0 0 24 24" aria-hidden="true"><path fill="var(--brand-green)" d="M2 9l10-6 10 6v11a1 1 0 0 1-1 1H3a1 1 0 0 1-1-1z"/><path fill="#fff" d="M4 10.2l8 5 8-5V19H4z"/></svg>
        <span>seoyun.park@arcvolley-example.co.kr</span>
      </div>
      <div class="contact contact--instagram">
        <svg viewBox="0 0 24 24" aria-hidden="true"><circle cx="12" cy="12" r="8" fill="var(--brand-green)"/></svg>
        <span>arcvolley</span>
      </div>
      <div class="contact contact--web">
        <svg viewBox="0 0 24 24" aria-hidden="true"><g fill="none" stroke="var(--brand-green)" stroke-width="1.8"><circle cx="12" cy="12" r="9"/><ellipse cx="12" cy="12" rx="4" ry="9"/><path d="M3 12h18"/></g></svg>
        <span>www.arcvolley-example.co.kr</span>
      </div>
      <div class="contact contact--address">
        <svg viewBox="0 0 24 24" aria-hidden="true"><path fill="var(--brand-green)" d="M12 2a7 7 0 0 0-7 7c0 5 7 13 7 13s7-8 7-13a7 7 0 0 0-7-7zm0 9.5A2.5 2.5 0 1 1 12 6.5a2.5 2.5 0 0 1 0 5z"/></svg>
        <span>경기도 용인시 수지구 풍덕천로 456 미래타워 5층 501호, 502호</span>
      </div>
    </div>
    <div class="band band--green"></div>
    <div class="band band--dark"></div>
  </section>

</div>
</body>
</html>
```